Brimford Accounting A5 flyer design

I need a flyer for a new company called Brimford Accounting. I am a self employed accountant and I provide the following services:VAT, Bookeeping, Personal Income Tax, Business Income Tax, Financial Accounting and Accounts Preparation.I am licenced by the GBL and need to include their logo and a statement, this is attached below.The licence wording has to be 8pt Arial Regular and the logo has to be 20mm.The kind of clients I want to attract are self employed traders and partnerships.

Target Market(s)

Self employed traders & partnerships

Industry/Entity Type

Accounting

Requirements
Must have
• Must have GBL logo & licence wording as attached

```html
<!DOCTYPE html>
<html lang="en">
<head>
<meta charset="UTF-8">
<title>Brimford Accounting – A5 Flyer</title>
<link rel="stylesheet" href="https://fonts.googleapis.com/css2?family=Playfair+Display:wght@700&family=EB+Garamond:wght@500&family=Delius&display=swap">
<style>
  :root {
    --navy: #0b4f9f;
    --sky: #8ccbef;
    --sky-text: #3fb0ea;
    --lime: #b2d235;
    --lime-pale: #d3e15a;
    --leaf: #2b9b3b;
    --white: #ffffff;
    --ink: #1f3b5c;
  }
  * { margin: 0; padding: 0; box-sizing: border-box; }
  html, body { width: 1200px; height: 846px; overflow: hidden; background: var(--white); }
  .flyer { position: relative; width: 1200px; height: 846px; overflow: hidden; background: var(--white); }
  .backdrop { position: absolute; inset: 0; }

  .brand-name {
    position: absolute; left: 22px; top: 92px;
    font-family: "Playfair Display", Georgia, serif; font-weight: 700;
    font-size: 104px; line-height: 1; letter-spacing: 1px;
    color: var(--navy);
    -webkit-text-stroke: 1px #b9d84a;
    text-shadow: 2px 2px 0 #c9de6a;
    white-space: nowrap;
  }

  .services { position: absolute; left: 394px; top: 252px; font-family: "EB Garamond", Georgia, serif; font-weight: 500; }
  .services-intro { font-size: 44px; line-height: 50px; color: var(--sky-text); margin-bottom: 4px; white-space: nowrap; }
  .services-list {
    font-size: 42px; line-height: 58px; color: var(--navy);
    text-shadow: 2px 2px 3px rgba(255,255,255,0.7);
    white-space: nowrap;
  }

  .contacts {
    position: absolute; left: 17px; top: 557px;
    font-family: "Delius", "Comic Sans MS", cursive; font-size: 24px; line-height: 43px;
    color: var(--white); list-style: none; white-space: nowrap;
  }

  .licence-note {
    position: absolute; left: 381px; top: 690px;
    font-family: Arial, Helvetica, sans-serif; font-size: 15px; line-height: 19.5px;
    color: var(--ink); white-space: nowrap;
  }

  .licensor-mark {
    position: absolute; left: 992px; top: 680px;
    font-family: "EB Garamond", Georgia, serif; font-weight: 500;
    font-size: 64px; line-height: 1; color: var(--leaf);
  }
</style>
</head>
<body>
<main class="flyer">
  <svg class="backdrop" width="1200" height="846" viewBox="0 0 1200 846" aria-hidden="true">
    <rect class="top-bar" x="0" y="0" width="1200" height="12" fill="var(--navy)"/>
    <rect class="side-sky" x="0" y="248" width="363" height="260" fill="var(--sky)"/>
    <circle class="side-disc" cx="182" cy="210" r="132" fill="var(--white)"/>
    <rect class="side-top-cut" x="0" y="12" width="363" height="236" fill="var(--white)"/>
    <rect class="side-navy" x="0" y="508" width="363" height="338" fill="var(--navy)"/>
    <rect class="services-panel" x="363" y="248" width="837" height="312" fill="var(--lime)"/>
    <rect class="services-strip" x="363" y="248" width="837" height="58" fill="var(--lime-pale)"/>
    <circle class="panel-disc" cx="1000" cy="602" r="133" fill="var(--white)"/>
    <rect class="panel-cut" x="363" y="560" width="837" height="200" fill="var(--white)"/>
    <path class="footer-wave" d="M800,800 C815,776 835,762 870,762 L1200,762 L1200,800 Z" fill="var(--sky)"/>
    <rect class="footer-band" x="363" y="799" width="837" height="47" fill="var(--lime)"/>
  </svg>

  <h1 class="brand-name">Brimford Accounting</h1>

  <section class="services">
    <p class="services-intro">We provide the following services:</p>
    <p class="services-list">VAT, Bookeeping, Personal Income<br>Tax, Business Income Tax,<br>Financial Accounting and<br>Accounts Preparation</p>
  </section>

  <ul class="contacts">
    <li>Our Contacts</li>
    <li>Tel:- 00000000000</li>
    <li>E-mail:-example@brimford.co</li>
    <li>Web:- www.xxxxxxxxxx.com</li>
  </ul>

  <p class="licence-note">Tessa Marlowe is licensed and regulated by GBL under licence number 2004719.<br>GBL is recognised by NR Treasury to supervise compliance with the Money<br>Laundering Regulations and Brimford Accounting is supervised by GBL in this respect.</p>

  <div class="licensor-mark">GBL</div>
</main>
</body>
</html>
```